K SPIRES Business Card Design

Need a business card design for K Spires, we're a tower company - our main scope of work is to upgrade cellular sites: swap antennas, install new coax, fiber, replace mounts, etc. Mostly tower work.

would like to see a sharp business card design with our logo either on background or with tower image on the background - something describing our field not only in words but in images.

Target Market(s)

USA

Industry/Entity Type

Business

Contact Information for Business Card

Tarik Benolven
Operations Manager
K Spires LLC

cell 404-555-0193
tarik@k-spires-example.com

2150 Harlowe Commerce Pkwy, Suite D
Norcross, GA, 30099

Requirements
Must have
• some tower related design
Nice to have
• some tower or cellular antennas on the background, if possible to compliment our logo...

```html
<!DOCTYPE html>
<html lang="en">
<head>
<meta charset="utf-8">
<title>K Spires Business Card</title>
<link rel="stylesheet" href="https://fonts.googleapis.com/css2?family=Saira+Condensed:wght@700&family=Exo+2:wght@400;500&display=swap">
<style>
  :root {
    --backdrop: #8e8e90;
    --brand-blue: #2e2484;
    --brand-green: #2f8c2c;
    --card-white: #f4f4f4;
    --card-shade: #dcdcdc;
    --ink: #2b2b2b;
    --paper: #ffffff;
  }
  * { margin: 0; padding: 0; box-sizing: border-box; }
  html, body {
    width: 1200px; height: 894px; overflow: hidden;
    background: var(--backdrop);
    font-family: "Exo 2", sans-serif;
  }
  .canvas { position: relative; width: 1200px; height: 894px; }

  .card {
    position: absolute; width: 700px; height: 400px; overflow: hidden;
    box-shadow: 0 10px 26px rgba(0,0,0,0.28);
  }

  /* Back side: brand */
  .card-back {
    left: 440px; top: 40px;
    background: linear-gradient(135deg, var(--paper), #ececec);
    display: flex; align-items: center; justify-content: center; gap: 22px;
  }
  .tower-mark {
    width: 64px; height: 64px;
    background: linear-gradient(180deg, var(--brand-green), #23701f);
  }
  .brand-name {
    font-family: "Exo 2", sans-serif; font-weight: 500;
    font-size: 84px; line-height: 1; color: var(--brand-blue); letter-spacing: 1px;
  }

  /* Front side: contact */
  .card-front {
    left: 60px; top: 454px;
    background: radial-gradient(ellipse at 45% 50%, var(--card-white) 0%, var(--card-shade) 100%);
  }
  .band { position: absolute; left: 0; width: 100%; background: var(--brand-blue); }
  .band-top { top: 0; height: 58px; border-bottom: 7px solid var(--brand-green); }
  .band-bottom { bottom: 0; height: 118px; border-top: 7px solid var(--brand-green); }

  .holder-name {
    position: absolute; left: 34px; top: 92px;
    font-family: "Saira Condensed", sans-serif; font-weight: 700;
    font-size: 48px; line-height: 1; color: var(--brand-green); letter-spacing: 1px;
  }
  .title-bar {
    position: absolute; left: 0; top: 146px; width: 318px; height: 58px;
    background: var(--brand-green); color: var(--paper);
    padding: 7px 0 0 34px;
  }
  .holder-title { font-size: 17px; font-weight: 500; letter-spacing: 1.5px; }
  .holder-site { font-size: 13px; margin-top: 3px; letter-spacing: 0.5px; }

  .contact-list {
    position: absolute; left: 370px; top: 84px; width: 300px; list-style: none;
  }
  .contact-item {
    display: flex; align-items: center; gap: 14px;
    height: 62px; color: var(--ink); font-size: 15px; line-height: 1.3;
  }
  .contact-icon {
    flex: none; width: 38px; height: 38px; border-radius: 50%;
    background: var(--brand-green);
    display: flex; align-items: center; justify-content: center;
  }
  .contact-icon svg { width: 20px; height: 20px; }
</style>
</head>
<body>
<main class="canvas">

  <section class="card card-back" aria-label="Card back">
    <span class="tower-mark" role="img" aria-label="Cell tower with antennas"></span>
    <span class="brand-name">K Spires</span>
  </section>

  <section class="card card-front" aria-label="Card front">
    <div class="band band-top"></div>
    <div class="band band-bottom"></div>

    <h1 class="holder-name">TARIK BENOLVEN</h1>
    <div class="title-bar">
      <p class="holder-title">OPERATIONS MANAGER</p>
      <p class="holder-site">www.k-spires-example.com</p>
    </div>

    <ul class="contact-list">
      <li class="contact-item">
        <span class="contact-icon">
          <svg viewBox="0 0 20 20" fill="none" stroke="#fff" stroke-width="2" stroke-linejoin="round">
            <path d="M2 10 L10 3 L18 10"/><path d="M5 8.5 V17 H15 V8.5"/><path d="M8.5 17 V12 H11.5 V17"/>
          </svg>
        </span>
        <span>2150 Harlowe Commerce Pkwy,<br>Suite D, Norcross, GA, 30099</span>
      </li>
      <li class="contact-item">
        <span class="contact-icon">
          <svg viewBox="0 0 20 20" fill="none" stroke="#fff" stroke-width="2">
            <rect x="6" y="2" width="8" height="16" rx="1.5"/><line x1="9" y1="15" x2="11" y2="15"/>
          </svg>
        </span>
        <span>404-555-0193</span>
      </li>
      <li class="contact-item">
        <span class="contact-icon">
          <svg viewBox="0 0 20 20" fill="none" stroke="#fff" stroke-width="2" stroke-linejoin="round">
            <rect x="2" y="5" width="16" height="11"/><path d="M2 5 L10 11 L18 5"/>
          </svg>
        </span>
        <span>tarik@k-spires-example.com</span>
      </li>
    </ul>
  </section>

</main>
</body>
</html>
```